Verdane Kiwi Root Essence Prime Serum - Product Label

Hi Guys,

I threw up a rough label sketch. Looking to keep the label clean and fresh.

LABEL DIMENSIONS: 4.05 in (Height) x 1.18 in (Diameter)

Industry/Entity Type

Beauty Aid

Font styles to use
Serif

Colors
0255a3
0592cd
6b449b
ffc214

Requirements
Must have
• Lumivelle
• __________
• S K I N
Nice to have
• We can try purple, gold and black or stick with the blue scheme we have going.

```html
<!DOCTYPE html>
<html lang="en">
<head>
<meta charset="utf-8">
<title>Verdane Kiwi Root Essence Prime Serum – Label</title>
<link rel="stylesheet" href="https://fonts.googleapis.com/css2?family=Cinzel:wght@400;600&family=Cormorant+SC:wght@500&display=swap">
<style>
  :root {
    --page-bg: #ececec;
    --label-bg: #ffffff;
    --navy: #1d2f7a;
    --royal: #0255a3;
    --sky: #0592cd;
    --mist: #dfe5f2;
    --wave-deep: #2e47a0;
  }
  * { margin: 0; padding: 0; box-sizing: border-box; }
  html, body {
    width: 852px;
    height: 1200px;
    overflow: hidden;
    background: var(--page-bg);
  }
  .canvas {
    position: relative;
    width: 852px;
    height: 1200px;
  }
  .label-panel {
    position: absolute;
    left: 251px;
    top: 50px;
    width: 350px;
    height: 1100px;
    background: var(--label-bg);
    overflow: hidden;
    box-shadow: 0 2px 10px rgba(0,0,0,0.08);
  }
  .top-band {
    position: absolute;
    left: 0;
    top: 40px;
    width: 100%;
    height: 7px;
    background: linear-gradient(90deg, var(--royal), var(--navy));
  }
  .veil-top {
    position: absolute;
    left: 0;
    top: 0;
    width: 100%;
    height: 240px;
    background: linear-gradient(200deg, var(--mist) 0%, rgba(255,255,255,0) 70%);
  }
  .brand-block {
    position: absolute;
    left: 0;
    top: 290px;
    width: 100%;
    text-align: center;
  }
  .brand-mark {
    display: inline-block;
    width: 14px;
    height: 14px;
    border-radius: 50%;
    background: var(--royal);
    margin-bottom: 14px;
  }
  .brand-name {
    font-family: "Cinzel", serif;
    font-weight: 600;
    font-size: 44px;
    letter-spacing: 2px;
    color: var(--navy);
    line-height: 1;
  }
  .product-name {
    margin-top: 22px;
    font-family: "Cormorant SC", serif;
    font-weight: 500;
    font-size: 21px;
    line-height: 1.15;
    letter-spacing: 0.5px;
    color: var(--royal);
  }
  .serum-pill {
    display: inline-block;
    margin-top: 18px;
    padding: 6px 22px 4px;
    border-radius: 22px;
    background: linear-gradient(180deg, var(--wave-deep), var(--navy));
    color: #ffffff;
    font-family: "Cinzel", serif;
    font-weight: 400;
    font-size: 22px;
    letter-spacing: 1px;
  }
  .volume {
    position: absolute;
    left: 0;
    top: 655px;
    width: 100%;
    text-align: center;
    font-family: "Cinzel", serif;
    font-size: 17px;
    letter-spacing: 1px;
    color: var(--royal);
  }
  .wave-field {
    position: absolute;
    left: 0;
    bottom: 0;
    width: 100%;
    height: 420px;
  }
</style>
</head>
<body>
<div class="canvas">
  <div class="label-panel">
    <div class="veil-top" role="img" aria-label="Faint translucent ribbon veils across the top of the label"></div>
    <div class="top-band"></div>

    <div class="brand-block">
      <span class="brand-mark"></span>
      <div class="brand-name">Lumivelle</div>
      <div class="product-name">Verdane Kiwi Root<br>Essence Prime</div>
      <div class="serum-pill">Serum</div>
    </div>

    <div class="volume">1 fl.oz/ 30ml</div>

    <svg class="wave-field" viewBox="0 0 350 420" role="img" aria-label="Flowing translucent blue ribbon waves sweeping across the lower label">
      <defs>
        <linearGradient id="waveTone" x1="0" y1="0" x2="0" y2="1">
          <stop offset="0" stop-color="#dfe5f2" stop-opacity="0"/>
          <stop offset="0.45" stop-color="#8ea0d4" stop-opacity="0.55"/>
          <stop offset="1" stop-color="#2e47a0" stop-opacity="0.85"/>
        </linearGradient>
      </defs>
      <rect x="0" y="0" width="350" height="420" fill="url(#waveTone)"/>
    </svg>
  </div>
</div>
</body>
</html>
```